Prominent Trial Lawyer need a Brochure Design for his firm

Douglas R. Pembry of The Pembry Law Firm has been successfully trying severe and complex for over 28 years. He holds the largest verdict in the history of South Georgia of $150,000,000.00 before the late Gerald T. Voskin in the Harlow District of the Lower District of Marren. He specializes in sever injuries, whether by auto accident, trucking accident or medical malpractice. He is also well know for his successful trial of business disputes and high net-worth Divorces.
Target Market(s)
Persons who need an aggressive, experienced trial lawyer especially for personal injury, but also for other civil and business matters, high end divorde
Industry/Entity Type
Medical
Contact Information for Business Card
Need to use coloring and logo uplaoded
Requirements
Must have
- 1) biography of principal, Douglas R. Pembry
- 2) what we do
- 3) specific cases handled, with specific outcomes (will be supplied)

```html
<!DOCTYPE html>
<html lang="en">
<head>
<meta charset="utf-8">
<title>The Pembry Law Firm – Trifold Brochure</title>
<link href="https://fonts.googleapis.com/css2?family=Lato:ital,wght@0,400;0,700;0,900;1,400&display=swap" rel="stylesheet">
<style>
  :root {
    --red: #d0171f;
    --red-dark: #b81219;
    --paper: #f3f3f1;
    --ink: #1e1e1e;
    --grey: #6b6b6b;
    --white: #ffffff;
    --stage: #e6e6e4;
    --photo-dark: #4a4f5a;
    --photo-light: #9fb0c8;
    --map-a: #5d6058;
    --map-b: #8a8c84;
  }
  * { box-sizing: border-box; margin: 0; padding: 0; }
  html, body { width: 1200px; height: 1000px; overflow: hidden; }
  body {
    background: var(--stage);
    font-family: 'Lato', sans-serif;
    color: var(--ink);
  }
  .brochure {
    position: absolute;
    left: 90px; top: 60px;
    width: 1020px; height: 880px;
    display: flex;
    box-shadow: 0 6px 24px rgba(0,0,0,.18);
  }
  .panel { position: relative; width: 340px; height: 100%; }

  /* Attorneys panel */
  .panel--attorneys { background: var(--red); color: var(--white); padding: 24px 22px; }
  .section-title { font-size: 19px; font-weight: 700; letter-spacing: .3px; }
  .rule { height: 3px; background: var(--white); }
  .rule--title { width: 230px; margin: 6px 0 0 -22px; }
  .attorney { display: flex; align-items: center; margin-top: 40px; gap: 16px; }
  .attorney--reverse { flex-direction: row-reverse; }
  .attorney-name { font-size: 27px; font-weight: 700; line-height: 1.2; flex: 1; }
  .attorney-name span { display: block; }
  .attorney-name .last { padding-left: 58px; }
  .attorney--reverse .attorney-name { padding-left: 10px; }
  .photo {
    width: 112px; height: 138px; border: 3px solid var(--white);
    flex: none;
  }
  .photo--senior { background: linear-gradient(160deg, var(--photo-light), var(--photo-dark)); }
  .photo--junior { background: linear-gradient(180deg, #e8e6e2 0%, #c9c2b8 55%, var(--photo-light) 100%); }
  .bio { font-size: 13.2px; line-height: 1.45; text-align: justify; margin-top: 14px; }
  .rule--divider { width: 180px; margin: 40px auto 0; }

  /* Contact panel */
  .panel--contact { background: var(--paper); padding: 28px 12px 0 14px; border-left: 1px solid #d8d8d6; border-right: 1px solid #d8d8d6; }
  .invite { font-style: italic; font-size: 16px; }
  .contact-head { font-size: 44px; color: var(--red); font-style: italic; font-weight: 400; line-height: 1.05; letter-spacing: -.5px; }
  .invite-more { font-style: italic; font-size: 15.5px; line-height: 1.25; }
  .rule--red { height: 3px; background: var(--red); margin: 14px -12px 0 -14px; width: 310px; }
  .help { color: var(--red); font-weight: 700; font-size: 17px; margin-top: 12px; }
  .call { font-size: 18px; margin-top: 48px; }
  .phone { color: var(--red); font-weight: 700; font-size: 29px; letter-spacing: 1.5px; margin-top: 16px; padding-left: 26px; }
  .map {
    width: 308px; height: 206px; margin: 30px 0 0 6px;
    background: linear-gradient(135deg, var(--map-a), var(--map-b) 50%, var(--map-a));
    border: 2px solid var(--white);
  }
  .location { font-size: 17px; line-height: 1.3; margin-top: 28px; }
  .address { color: var(--red); font-size: 20px; line-height: 1.3; margin-top: 12px; padding-left: 26px; }
  .web-band {
    position: absolute; left: 0; right: 0; bottom: 56px; height: 38px;
    background: var(--red); color: var(--white);
    display: flex; align-items: center; justify-content: center;
    font-weight: 700; font-size: 15px; letter-spacing: 3px;
  }

  /* Cover panel */
  .panel--cover { background: var(--paper); text-align: center; }
  .brand-mark { position: absolute; top: 176px; left: 50%; transform: translateX(-50%); }
  .brand-name {
    position: absolute; top: 372px; left: 0; right: 0;
    font-size: 40px; font-weight: 700; line-height: 1.1; color: var(--ink);
    letter-spacing: 1px;
  }
  .brand-tag { position: absolute; top: 472px; left: 0; right: 0; color: var(--red); font-size: 19px; letter-spacing: .5px; }
  .quote {
    position: absolute; left: 30px; right: 28px; top: 700px;
    text-align: left; font-style: italic; color: var(--grey); font-size: 17px; line-height: 1.4;
  }
  .quote-by { display: block; text-align: right; font-size: 13px; margin-top: 18px; }
</style>
</head>
<body>
  <main class="brochure">
    <section class="panel panel--attorneys">
      <h2 class="section-title">Our Attorneys</h2>
      <div class="rule rule--title"></div>

      <article class="attorney">
        <h3 class="attorney-name"><span>Douglas</span><span class="last">Pembry</span></h3>
        <div class="photo photo--senior" role="img" aria-label="Portrait photo of Douglas Pembry"></div>
      </article>
      <p class="bio">Douglas graduated with honors from the University of Marren School of Law in 1986. He also received his BBA from UM in 1982. Douglas has spent the last 26 years trying complex cases, including medical malpractice, personal injury, criminal and civil cases. He holds the largest verdict in the Lower District of Marren of $150,000,000.00. Currently he specializes in severe personal injury cases and commercial litigation.</p>

      <div class="rule rule--divider"></div>

      <article class="attorney attorney--reverse">
        <h3 class="attorney-name"><span>J. Martin</span><span class="last">Hale</span></h3>
        <div class="photo photo--junior" role="img" aria-label="Portrait photo of J. Martin Hale"></div>
      </article>
      <p class="bio">Martin is a native of Alder Creek, Marren, and a graduate of Alder County High School. He graduated from the University of Marren in 2009 with a Bachelor of Business Administration in Real Estate. He then attended the University of Marren School of Law where he earned a J.D. and graduated in 2012. Martin is married to Laura Hale who works as a school counselor at Alder Creek Elementary School. They are expecting the birth of their first child in November of this year.</p>
    </section>

    <section class="panel panel--contact">
      <p class="invite">We invite you to</p>
      <h2 class="contact-head">CONTACT US</h2>
      <p class="invite-more">with your particular legal matters whenever they may arise.</p>
      <div class="rule--red"></div>
      <p class="help">WE'RE ALWAYS HERE TO HELP.</p>
      <p class="call">You may call us at:</p>
      <p class="phone">(555) 014.3920</p>
      <div class="map" role="img" aria-label="Aerial street map of downtown Harlow showing the office location"></div>
      <p class="location">The Pembry Law firm is located in the heart of Harlow, Mr.</p>
      <p class="address">240 Linden Ave Harlow, MR 30155</p>
      <div class="web-band">www.pembrylawfirm.com</div>
    </section>

    <section class="panel panel--cover">
      <svg class="brand-mark" width="150" height="150" viewBox="0 0 150 150" aria-hidden="true">
        <circle cx="75" cy="75" r="66" fill="none" stroke="var(--red)" stroke-width="6"/>
      </svg>
      <h1 class="brand-name">The Pembry<br>Law Firm</h1>
      <p class="brand-tag">TRIAL LAWYER</p>
      <blockquote class="quote">“Whether you are against Insurance Companies, Fortune 500 Companies or Goverments, we level the field and give you the edge.”
        <span class="quote-by">- The Pembry Law Firm</span>
      </blockquote>
    </section>
  </main>
</body>
</html>
```